BRIGHTWAVE PARTNERS NAMECARD

Need to design a name card with an existing logo.

As we are professional corporate services provider our name card has to project a professional image.
Should be corporate, simple & professional.

Our corporate color is maroon red but not too dull.

Please refer to our website at www.brightwavepartners.com.sg

Would attach our logo herewith.

Front surface of namecard details:
BRIGHTWAVE PARTNERS PTE LTD
Registration No. 208731945K

Lowe Hui Ting CA (Singapore)
Director

Tel +65 6481 2957
Mobile +65 9172 3806
lowe@brightwavepartners.com.sg
www.brightwavepartners.com.sg

47 Palmer Lane
#07-14 Harbourlight Plaza
Singapore 274153

Back of namecard:-
OUR CORE SERVICES
Incorporation services
Corporate Secretarial Services
Accountancy service
Goods & Services Taxation
Corporate & Personal Taxation
Financial Reporting
Payroll Administration

AFFILIATES:
TRIVANTA CORPORATE SERVICES PTE LTD
BRIGHTWAVEREGISTRYPTE LTD
ORR MANAGEMENT SERVICES PTE LTD
DW LIM AND COMPANY PTE LTD
LEDGERWISE ACADEMY

```html
<!DOCTYPE html>
<html lang="en">
<head>
<meta charset="utf-8">
<title>Brightwave Partners Stationery</title>
<link rel="stylesheet" href="https://fonts.googleapis.com/css2?family=EB+Garamond:wght@400;600&family=Open+Sans:wght@400&display=swap">
<style>
  :root {
    --brand-red: #d01f2e;
    --paper: #ffffff;
    --backdrop: #d4d4d4;
    --ink: #4a4a4a;
    --window: #eeeeee;
  }
  * { margin: 0; padding: 0; box-sizing: border-box; }
  html, body { width: 1200px; height: 1200px; overflow: hidden; background: var(--backdrop); }
  .canvas { position: relative; width: 1200px; height: 1200px; font-family: "EB Garamond", Georgia, serif; }
  .sheet { position: absolute; background: var(--paper); }

  /* Company name placeholder: plain text with a single square marker */
  .brand-name { position: absolute; display: flex; align-items: center; gap: .35em; font-family: "EB Garamond", Georgia, serif; font-weight: 400; color: var(--brand-red); white-space: nowrap; line-height: 1; }
  .brand-name .brand-square { width: .6em; height: .6em; background: currentColor; flex: none; }

  /* Letterhead */
  .letterhead { left: 164px; top: 344px; width: 399px; height: 521px; }
  .letterhead .brand-name { top: 22px; left: 50%; transform: translateX(-50%); font-size: 20px; }
  .letter-body { position: absolute; left: 23px; top: 192px; width: 345px; font-family: "Open Sans", Arial, sans-serif; font-size: 7.4px; line-height: 13px; color: var(--ink); }
  .letter-body p { margin-bottom: 8px; }
  .letter-footer { position: absolute; left: 0; bottom: 0; width: 100%; height: 48px; background: var(--brand-red); color: var(--paper); font-size: 7.4px; line-height: 8px; }
  .letter-footer .address { position: absolute; left: 23px; top: 7px; }
  .letter-footer .contact { position: absolute; left: 266px; top: 5px; }

  /* Name card */
  .namecard { left: 734px; top: 319px; width: 248px; height: 144px; }
  .namecard .brand-name { right: 13px; top: 11px; font-size: 12px; }
  .card-person { position: absolute; left: 12px; top: 28px; color: var(--brand-red); }
  .card-person .name { font-size: 8.6px; line-height: 9px; }
  .card-person .title { font-size: 6px; line-height: 8px; }
  .card-person .address { margin-top: 2px; font-size: 4.6px; line-height: 5.6px; padding-left: 7px; position: relative; }
  .card-contact { position: absolute; left: 160px; top: 40px; color: var(--brand-red); font-size: 4.6px; line-height: 5.8px; }
  .card-rule { position: absolute; left: 12px; right: 12px; top: 73px; height: 1px; background: var(--brand-red); }
  .card-col { position: absolute; top: 84px; color: var(--brand-red); }
  .card-col h3 { font-size: 6px; font-weight: 600; line-height: 7px; }
  .card-col li { list-style: none; font-size: 4.3px; line-height: 5.2px; font-weight: 600; }
  .services { left: 12px; }
  .affiliates { left: 128px; }

  .icon { display: inline-block; vertical-align: middle; fill: var(--brand-red); flex: none; }
  .row { display: flex; align-items: center; gap: 3px; }

  /* Envelope back */
  .envelope-back { left: 662px; top: 502px; width: 377px; height: 178px; }
  .envelope-back .flap { position: absolute; left: 0; top: 0; width: 377px; height: 35px; }
  .envelope-back .brand-name { top: 12px; left: 50%; transform: translateX(-50%); font-size: 10px; color: var(--paper); }

  /* Envelope front */
  .envelope-front { left: 662px; top: 694px; width: 377px; height: 177px; }
  .envelope-front .brand-name { left: 21px; top: 26px; font-size: 22px; }
  .envelope-front .contact { position: absolute; left: 21px; top: 82px; color: var(--brand-red); font-size: 8.4px; line-height: 8.8px; }
  .envelope-front .contact .indent { padding-left: 10px; }
  .address-window { position: absolute; left: 240px; top: 117px; width: 101px; height: 36px; border-radius: 5px; background: var(--window); }
  .envelope-front .rule-thick { position: absolute; left: 0; width: 100%; top: 161px; height: 3px; background: var(--brand-red); }
  .envelope-front .rule-thin { position: absolute; left: 0; width: 100%; top: 167px; height: 1px; background: var(--brand-red); }
</style>
</head>
<body>
<main class="canvas">

  <section class="sheet letterhead">
    <div class="brand-name"><span class="brand-square"></span>Brightwave Partners</div>
    <div class="letter-body">
      <p>Dear [Recipient],</p>
      <p>We love the look of this stationery just the way it is. But you can add your own personal touch in almost no time.</p>
      <p>On the Design tab of the ribbon, check out the Themes, Colors, and Fonts galleries to preview different looks from a variety of choices. Then just click to apply the one you like.</p>
      <p>We've also created styles that let you match the formatting you see in this letter with just a click. On the Home tab of the ribbon, check out the Styles gallery for all styles used in this letter.</p>
      <p>Ready to add your digits? No problem. Just double click the header area to add your contact information.</p>
      <p style="margin-bottom:0">Warm regards,<br>Renata</p>
    </div>
    <footer class="letter-footer">
      <div class="address">47 Palmer Lane<br>#07-14 Harbourlight Plaza<br>Singapore 274153</div>
      <div class="contact">+65 6481 2957<br>+65 9172 3806<br>lowe@brightwavepartners.com.sg<br>www.brightwavepartners.com.sg</div>
    </footer>
  </section>

  <section class="sheet namecard">
    <div class="brand-name"><span class="brand-square"></span>Brightwave Partners</div>
    <div class="card-person">
      <div class="name">Lowe Hui Ting CA</div>
      <div class="title">Director</div>
      <div class="address">
        <svg class="icon" style="position:absolute;left:0;top:1px" width="4" height="5" viewBox="0 0 10 14"><path d="M5 0a5 5 0 0 0-5 5c0 4 5 9 5 9s5-5 5-9a5 5 0 0 0-5-5zm0 7a2 2 0 1 1 0-4 2 2 0 0 1 0 4z"/></svg>
        47 Palmer Lane<br>#07-14 Harbourlight Plaza<br>Singapore 274153
      </div>
    </div>
    <div class="card-contact">
      <div class="row"><svg class="icon" width="4" height="4" viewBox="0 0 10 10"><path d="M2 0l2 2-1 2c1 1 2 2 3 3l2-1 2 2-2 2C4 10 0 6 0 2z"/></svg>+65 6481 2957</div>
      <div class="row"><svg class="icon" width="4" height="4" viewBox="0 0 10 10"><path d="M2 0h6v10H2zm1 1v7h4V1z"/></svg>+65 9172 3806</div>
      <div class="row"><svg class="icon" width="4" height="4" viewBox="0 0 10 10"><path d="M0 2h10v6H0zm1 1l4 3 4-3z"/></svg>lowe@brightwavepartners.com.sg</div>
      <div class="row"><svg class="icon" width="4" height="4" viewBox="0 0 10 10"><circle cx="5" cy="5" r="5"/></svg>www.brightwavepartners.com.sg</div>
    </div>
    <div class="card-rule"></div>
    <div class="card-col services">
      <h3>OUR CORE SERVICES</h3>
      <ul>
        <li>Incorporation services</li>
        <li>Corporate Secretarial Services</li>
        <li>Accountancy service</li>
        <li>Goods &amp; Services Taxation</li>
        <li>Corporate &amp; Personal Taxation</li>
        <li>Financial Reporting</li>
        <li>Payroll Administration</li>
      </ul>
    </div>
    <div class="card-col affiliates">
      <h3>AFFILIATES:</h3>
      <ul>
        <li>TRIVANTA CORPORATE SERVICES PTE LTD</li>
        <li>BRIGHTWAVEREGISTRYPTE LTD</li>
        <li>ORR MANAGEMENT SERVICES PTE LTD</li>
        <li>DW LIM AND COMPANY PTE LTD</li>
        <li>LEDGERWISE ACADEMY</li>
      </ul>
    </div>
  </section>

  <section class="sheet envelope-back">
    <svg class="flap" viewBox="0 0 377 35" preserveAspectRatio="none"><polygon points="0,0 377,0 377,2 360,35 17,35 0,2" fill="var(--brand-red)"/></svg>
    <div class="brand-name"><span class="brand-square"></span>Brightwave Partners</div>
  </section>

  <section class="sheet envelope-front">
    <div class="brand-name"><span class="brand-square"></span>Brightwave Partners</div>
    <div class="contact">
      <div class="row"><svg class="icon" width="7" height="8" viewBox="0 0 10 14"><path d="M5 0a5 5 0 0 0-5 5c0 4 5 9 5 9s5-5 5-9a5 5 0 0 0-5-5zm0 7a2 2 0 1 1 0-4 2 2 0 0 1 0 4z"/></svg><span>47 Palmer Lane</span></div>
      <div class="indent">#07-14 Harbourlight Plaza</div>
      <div class="indent">Singapore 274153</div>
      <div class="row"><svg class="icon" width="7" height="7" viewBox="0 0 10 10"><path d="M2 0l2 2-1 2c1 1 2 2 3 3l2-1 2 2-2 2C4 10 0 6 0 2z"/></svg><span>+65 6481 2957</span></div>
      <div class="row"><svg class="icon" width="7" height="7" viewBox="0 0 10 10"><path d="M2 0h6v10H2zm1 1v7h4V1z"/></svg><span>+65 9172 3806</span></div>
      <div class="row"><svg class="icon" width="7" height="7" viewBox="0 0 10 10"><path d="M0 2h10v6H0zm1 1l4 3 4-3z"/></svg><span>lowe@brightwavepartners.com.sg</span></div>
      <div class="row"><svg class="icon" width="7" height="7" viewBox="0 0 10 10"><circle cx="5" cy="5" r="5"/></svg><span>www.brightwavepartners.com.sg</span></div>
    </div>
    <div class="address-window"></div>
    <div class="rule-thick"></div>
    <div class="rule-thin"></div>
  </section>

</main>
</body>
</html>
```